Accounting Practice Business Card Design

I have a logo I am happy for you to use in the design of the Business Card.
You can edit and change colours as you please, I am not fixated on it.
I am looking for a modern and clean overall feel for the finished design.

The business is a small accounting practice who thrives on word of mouth referrals and this card will be given to all current and prospect clients.

Industry/Entity Type

Accountant

Contact Information for Business Card

Marcus Elwin
Level 5, 8 Corvale Ridge Road
ASHGROVE RISE VIC 3187
Phone: 9481 3057
Email: melwin@mrfaccountants.com.au
Web: www.mrfaccountants.com.au

Font styles to use
Serif
Sans Serif

Colors
0555a3
3277b5
85acd3
0393ce
33a6d7
85cae6
00a990
33b8a4
9bcb3c

Requirements
Must have
• "The end to your tax problems begin with us"
• "A referral from you is our greatest compliment"
Nice to have
• Modern clean professional

```html
<!DOCTYPE html>
<html lang="en">
<head>
<meta charset="utf-8">
<title>MRF Accountants – Business Cards</title>
<link href="https://fonts.googleapis.com/css2?family=Michroma&family=Arimo:wght@400;700&display=swap" rel="stylesheet">
<style>
  :root {
    --page-bg: #1c1c1c;
    --card-bg: #2a2a2a;
    --brand-blue: #0b5aa0;
    --brand-green: #3b8b3d;
    --brand-navy: #2c3489;
    --text-light: #f2f2f2;
  }
  * { box-sizing: border-box; margin: 0; padding: 0; }
  html, body { width: 1200px; height: 900px; overflow: hidden; }
  body {
    background: var(--page-bg);
    font-family: "Arimo", Arial, sans-serif;
    position: relative;
  }
  .card {
    position: absolute;
    left: 260px;
    width: 680px;
    height: 389px;
    background: var(--card-bg);
    border-radius: 16px;
    overflow: hidden;
    box-shadow: 0 10px 30px rgba(0,0,0,.5);
  }
  .card--front { top: 40px; }
  .card--back { top: 471px; }

  .brand-name {
    font-family: "Michroma", "Arimo", sans-serif;
    color: var(--brand-blue);
    text-transform: uppercase;
    white-space: nowrap;
    display: flex;
    align-items: center;
  }
  .brand-mark {
    display: inline-block;
    background: var(--brand-blue);
    border-radius: 50%;
  }
  .card--front .brand-name {
    position: absolute;
    top: 105px;
    left: 0; right: 0;
    justify-content: center;
    font-size: 34px;
    gap: 16px;
  }
  .card--front .brand-mark { width: 26px; height: 26px; }

  .band {
    position: absolute;
    left: 0; right: 0;
    display: flex;
    align-items: center;
    justify-content: center;
    color: var(--text-light);
    font-weight: 700;
    text-transform: uppercase;
    font-size: 15px;
    letter-spacing: .3px;
  }
  .band--referral { top: 246px; height: 68px; background: var(--brand-green); }
  .band--promise { top: 314px; height: 75px; background: var(--brand-navy); align-items: flex-start; padding-top: 10px; }

  .card--back .brand-name {
    position: absolute;
    top: 50px;
    right: 44px;
    font-size: 22px;
    gap: 10px;
  }
  .card--back .brand-mark { width: 16px; height: 16px; }

  .person { position: absolute; top: 118px; left: 46px; }
  .person__name { color: var(--brand-green); font-size: 20px; text-transform: uppercase; letter-spacing: .3px; }
  .person__role { color: var(--text-light); font-size: 16px; margin-top: 4px; }

  .contact-list { position: absolute; left: 46px; top: 270px; list-style: none; }
  .contact-list li { display: flex; align-items: center; gap: 12px; color: var(--text-light); font-size: 16px; height: 26px; }
  .contact-list svg { width: 16px; height: 16px; fill: var(--brand-green); }
  .contact-list .contact-web { color: var(--brand-green); padding-left: 28px; font-size: 17px; }

  .address {
    position: absolute;
    right: 44px;
    top: 232px;
    text-align: right;
    color: var(--brand-green);
    font-size: 15px;
    line-height: 1.45;
  }
  .address__city { text-transform: uppercase; }

  .edge-stripe { position: absolute; left: 0; right: 0; bottom: 0; height: 8px; display: flex; }
  .edge-stripe__navy { flex: 0 0 60%; background: var(--brand-navy); }
  .edge-stripe__green { flex: 1; background: var(--brand-green); }
</style>
</head>
<body>
  <section class="card card--front" aria-label="Card front">
    <div class="brand-name"><span class="brand-mark"></span>MRF Accountants</div>
    <div class="band band--referral">A referral from you is our greatest compliment</div>
    <div class="band band--promise">The end to your tax problems begin with us</div>
  </section>

  <section class="card card--back" aria-label="Card back">
    <div class="brand-name"><span class="brand-mark"></span>MRF Accountants</div>
    <div class="person">
      <p class="person__name">Marcus Elwin</p>
      <p class="person__role">Managing Director</p>
    </div>
    <ul class="contact-list">
      <li>
        <svg viewBox="0 0 24 24" aria-hidden="true"><path d="M6.6 10.8a15.1 15.1 0 0 0 6.6 6.6l2.2-2.2c.3-.3.7-.4 1-.2 1.1.4 2.3.6 3.6.6.6 0 1 .4 1 1V20c0 .6-.4 1-1 1A17 17 0 0 1 3 4c0-.6.4-1 1-1h3.5c.6 0 1 .4 1 1 0 1.3.2 2.5.6 3.6.1.3 0 .7-.2 1z"/></svg>
        9481 3057
      </li>
      <li>
        <svg viewBox="0 0 24 24" aria-hidden="true"><path d="M2 5h20v14H2z M3 6l9 7 9-7" fill="none" stroke="#3b8b3d" stroke-width="2"/></svg>
        melwin@mrfaccountants.com.au
      </li>
      <li class="contact-web">www.mrfaccountants.com.au</li>
    </ul>
    <address class="address" style="font-style:normal">
      <span>Level 5, 8 Corvale Ridge Road</span><br>
      <span class="address__city">Ashgrove Rise VIC 3187</span>
    </address>
    <div class="edge-stripe"><span class="edge-stripe__navy"></span><span class="edge-stripe__green"></span></div>
  </section>
</body>
</html>
```